Paraffin Wax Packaging Design for Nail and Beauty Industry

We need an attractive design for the packaging of our new product, Paraffin Wax. Our company is a wholesale beauty/nail supply company that has been selling to nail salons in the US market for 10 years. We currently sell this product that we buy from another company. Now we want to launch our own brand of Paraffin Wax.

Target Market(s)

Retail nail salons in the US market.

Industry/Entity Type

Industry

Font styles to use
Sans Serif

Colors

Designer to choose colors to be used in the design.

Requirements
Must have
• Our logo (attached).
• All information on the "Ingredient List" (attached).
• Design for Clear Packaging so product can show through.
• Design for Package Dimensions of 4.25" x 11" (110cm x 280 cm).
Nice to have
• Picture related to women's skin and or beauty.
• Contrast as in the design of product that we currently sell (attached).

```html
<!DOCTYPE html>
<html lang="en">
<head>
<meta charset="utf-8">
<title>Paraffin Wax Packaging</title>
<link href="https://fonts.googleapis.com/css2?family=Amatic+SC:wght@700&family=PT+Sans:wght@400;700&display=swap" rel="stylesheet">
<style>
  :root {
    --page-bg: #ffffff;
    --pack-bg: #e4e4e6;
    --pack-top: #ececee;
    --ink-navy: #161c5c;
    --ink-body: #2b2a86;
    --blue-light: #00aeea;
    --blue-deep: #0073a6;
    --purple-light: #8a5ba8;
    --purple-deep: #6a3e97;
  }
  * { margin: 0; padding: 0; box-sizing: border-box; }
  html, body {
    width: 1200px; height: 1200px; overflow: hidden;
    background: var(--page-bg);
  }
  .canvas { position: relative; width: 1200px; height: 1200px; }
  .pack {
    position: absolute; left: 414px; top: 82px;
    width: 376px; height: 1016px;
    background: var(--pack-bg);
    border-top: 38px solid var(--pack-top);
    border-bottom: 18px solid var(--pack-top);
  }
  .hero { display: block; width: 376px; height: 312px; }
  .title {
    margin-top: 14px;
    font-family: "Amatic SC", sans-serif;
    font-weight: 700;
    font-size: 66px;
    line-height: 54px;
    letter-spacing: 2px;
    text-align: center;
    color: var(--ink-navy);
  }
  .copy {
    width: 260px; margin: 22px auto 0;
    font-family: "PT Sans", sans-serif;
    font-size: 18.5px; line-height: 20.5px;
    color: var(--ink-body);
    text-align: justify; text-align-last: center;
  }
  .copy p + p { margin-top: 20px; }
  .copy .strong { font-weight: 700; }
  .copy .label { font-weight: 700; }
  .brand {
    margin-top: 18px; text-align: center;
    font-family: "PT Sans", sans-serif;
    font-weight: 700; font-size: 38px;
    color: var(--ink-navy);
  }
  .net-band {
    position: absolute; left: 0; right: 0; bottom: 16px;
    height: 34px;
    background: linear-gradient(90deg, var(--purple-light), var(--purple-deep));
    font-family: "PT Sans", sans-serif; font-weight: 700;
    font-size: 17px; line-height: 34px; text-align: center;
    color: var(--ink-navy);
  }
</style>
</head>
<body>
<div class="canvas">
  <div class="pack">
    <svg class="hero" viewBox="0 0 376 312" role="img" aria-label="Illustration of a woman's profile in blue and purple tones">
      <defs>
        <linearGradient id="heroTone" x1="0" y1="0" x2="1" y2="0">
          <stop offset="0" stop-color="var(--blue-light)"/>
          <stop offset="0.45" stop-color="var(--blue-deep)"/>
          <stop offset="0.55" stop-color="var(--purple-light)"/>
          <stop offset="1" stop-color="var(--purple-deep)"/>
        </linearGradient>
      </defs>
      <path d="M0 0 H366 V312 H270 C150 318 30 250 0 112 Z" fill="url(#heroTone)"/>
    </svg>

    <h1 class="title">Paraffin<br>Wax</h1>

    <div class="copy">
      <p class="strong">Compatible for use with most wax paraffin heat therapy units.</p>
      <p class="strong">Deeply Moisturizes the Skin Restoring a Healthier Look and Feel to Skin.</p>
      <p><span class="label">Ingredients:</span> Paraffin waxes and Hydrocarbon waxes, Petrolatum, Paraffin oils, Apricot kernel oil, Fragrance D &amp; C dyes.</p>
      <p><span class="label">Caution:</span> Paraffin is flammable. Do not use near open flame or an unprotected resistance heater.</p>
    </div>

    <div class="brand">By Lumera</div>

    <div class="net-band">Net Wt. 1 lb. (450 g.)</div>
  </div>
</div>
</body>
</html>
```